Fur Kit Hub Business Card Design Project

Hi All,

I need a business card /logo design.

The name of my upcoming business will be FurKitHub.example (e-commerce biz, thus name of business is same as website).

FurKitHub.example
Derek Lonsdale/Owner
tel# 555-017-4682
Elmbrook Falls, ST 00000

I'm definitely open to design creativity. However, one idea that I envisioned was to have a fun cartoon animals, like maybe a dog leaning on the 'P' and a cat leaning on the 'm' and a bird standing on the 't' or 'g'. Thank you in advance!

I need a catchy slogan added to my card. I appreciate your ideas. I don't want it to isolate dog or cat or bird etc...TY!

Hi All, The name of my upcoming business will be FurKitHub.example (e-commerce biz, thus name of business is same as website) I need a business card design/logo. Elmbrook Falls, ST 00000 tel# 555-017-4682 Derek Lonsdale/Owner I'm definitely open to design creativity. However, one idea that I envisioned was to have a fun cartoon animals, like maybe a dog leaning on the 'P' and a cat leaning on the 'm' and a bird standing on the 't' or 'g'. Thank you in advance!

Hi All! I need a catchy slogan added to my card. I appreciate your ideas. I don't want it to isolate dog or cat or bird etc...TY!

```html
<!DOCTYPE html>
<html lang="en">
<head>
<meta charset="utf-8">
<title>Fur Kit Hub Business Card</title>
<link rel="stylesheet" href="https://fonts.googleapis.com/css2?family=Open+Sans:wght@400;700&display=swap">
<style>
  :root {
    --page-bg: #e6e7ea;
    --card-bg: #ffffff;
    --brand-blue: #1b5a94;
    --ink: #1a1a1a;
    --divider: #111111;
    --band-light: #cfe3f4;
    --band-mid: #2a6fb8;
    --band-navy: #27308a;
  }
  * { margin: 0; padding: 0; box-sizing: border-box; }
  html, body {
    width: 1200px; height: 999px; overflow: hidden;
    background: var(--page-bg);
    font-family: "Open Sans", Arial, sans-serif;
  }
  .card {
    position: absolute; left: 74px; top: 197px;
    width: 1051px; height: 605px;
    background: var(--card-bg);
    overflow: hidden;
  }
  .card-band {
    position: absolute; left: 0; top: 380px;
    width: 1051px; height: 225px;
    background: linear-gradient(to bottom, rgba(255,255,255,0) 0%, var(--band-light) 30%, var(--band-mid) 70%, var(--band-navy) 100%);
  }
  .brand {
    position: absolute; left: 112px; top: 306px;
    display: flex; align-items: center; gap: 14px;
  }
  .brand-dot {
    width: 30px; height: 30px; border-radius: 50%;
    background: var(--brand-blue);
  }
  .brand-name {
    font-weight: 700; font-size: 50px; line-height: 1;
    color: var(--brand-blue); letter-spacing: -0.5px;
  }
  .divider {
    position: absolute; left: 502px; top: 133px;
    width: 2px; height: 275px; background: var(--divider);
  }
  .contact { position: absolute; left: 638px; top: 166px; color: var(--ink); }
  .contact-name {
    font-weight: 700; font-size: 35px; line-height: 1.1;
    color: var(--brand-blue);
  }
  .contact-role { font-size: 24px; line-height: 1.3; margin-top: 2px; }
  .contact-address { font-size: 24px; margin-top: 34px; line-height: 1.3; }
  .contact-line {
    display: flex; align-items: center; gap: 16px;
    font-size: 24px; margin-top: 13px; line-height: 1.3;
  }
  .contact-icon { width: 24px; height: 24px; flex: none; }
</style>
</head>
<body>
  <div class="card">
    <div class="card-band" role="img" aria-label="Decorative blue band along the bottom of the card"></div>

    <div class="brand">
      <span class="brand-dot"></span>
      <span class="brand-name">Fur Kit Hub</span>
    </div>

    <div class="divider"></div>

    <div class="contact">
      <div class="contact-name">Derek Lonsdale</div>
      <div class="contact-role">Owner</div>
      <div class="contact-address">Elmbrook Falls, ST 00000</div>
      <div class="contact-line">
        <svg class="contact-icon" viewBox="0 0 24 24" aria-hidden="true">
          <path fill="var(--brand-blue)" d="M6.6 10.8a15.1 15.1 0 0 0 6.6 6.6l2.2-2.2a1 1 0 0 1 1-.25 11.4 11.4 0 0 0 3.6.57 1 1 0 0 1 1 1V20a1 1 0 0 1-1 1A17 17 0 0 1 3 4a1 1 0 0 1 1-1h3.5a1 1 0 0 1 1 1c0 1.25.2 2.45.57 3.57a1 1 0 0 1-.25 1z"/>
          <path fill="none" stroke="var(--brand-blue)" stroke-width="1.8" stroke-linecap="round" d="M14 3.5a7 7 0 0 1 6.5 6.5M14 7a3.5 3.5 0 0 1 3 3"/>
        </svg>
        <span>555-017-4682</span>
      </div>
      <div class="contact-line">
        <svg class="contact-icon" viewBox="0 0 24 24" aria-hidden="true">
          <circle cx="12" cy="12" r="10" fill="var(--brand-blue)"/>
          <g fill="none" stroke="#fff" stroke-width="1.3">
            <ellipse cx="12" cy="12" rx="4.2" ry="10"/>
            <path d="M2 12h20M3.5 7h17M3.5 17h17M12 2v20"/>
          </g>
        </svg>
        <span>FurKitHub.example</span>
      </div>
    </div>
  </div>
</body>
</html>
```